lumenweave project business card, interior design and decoration firm

I'm a young woman and I've just created my interior design consulting firm. I'm very inspired by brasilian design, italian design, argentinian spirit, I like pure forms, chic colors (blue specially) and raw stuffs (wood, glass,
I work with wines properties, boats and yachts dealers, private people. Elegant but inspired
It's very important to dedicate one side to this card to the name Lumenweave. I would like my name on the other side (Claire-Anne Vobrel), my mail cavobrel@postvane.fr, my number + 33 6 91 35 20 86

Target Market(s)

middle and upper class, young people,

Contact Information for Business Card

Font styles to use
Sans Serif

Colors
0255a3
85abd2
000000
fdfdfd
86cfc6
fdf0f6
00a990
f04a50

Requirements
Must have
• The name Lumenweave, my name my number and mail one or two colors max, one logo if it's possible. AND uder The name Lumenweave "Cabinet de conseil en aménagement intérieur"

```html
<!DOCTYPE html>
<html lang="fr">
<head>
<meta charset="utf-8">
<title>Lumenweave – carte de visite</title>
<link rel="stylesheet" href="https://fonts.googleapis.com/css2?family=Questrial&display=swap">
<style>
  :root {
    --backdrop: #2b2b2d;
    --navy: #14244b;
    --navy-deep: #0f1c3d;
    --navy-glow: #1c2f5e;
    --paper: #fdfdfd;
    --mist: #e9e9ec;
    --blush: #f3e4ea;
    --ink: #14244b;
  }
  html, body {
    margin: 0;
    padding: 0;
    width: 1200px;
    height: 880px;
    overflow: hidden;
    background: var(--backdrop);
    font-family: "Questrial", "Century Gothic", sans-serif;
  }
  .canvas {
    position: relative;
    width: 1200px;
    height: 880px;
  }
  .card {
    position: absolute;
    width: 640px;
    height: 380px;
    border-radius: 22px;
    overflow: hidden;
    box-shadow: 0 18px 40px rgba(0,0,0,0.45);
  }
  .card--front {
    left: 100px;
    top: 40px;
    background: var(--navy);
  }
  .card--back {
    left: 460px;
    top: 460px;
    background: var(--paper);
  }
  .front-texture {
    position: absolute;
    inset: 0;
    background: radial-gradient(circle at 48% 48%, var(--navy-glow) 0%, var(--navy) 45%, var(--navy-deep) 100%);
  }
  .front-lockup {
    position: absolute;
    left: 0;
    right: 0;
    top: 122px;
    text-align: center;
    color: var(--paper);
  }
  .brand {
    margin: 0;
    font-weight: 400;
    font-size: 76px;
    letter-spacing: -0.5px;
    line-height: 1;
  }
  .tagline {
    margin: 18px 0 0;
    font-size: 18px;
    letter-spacing: 0.3px;
    padding-left: 40px;
  }
  .back-photo {
    position: absolute;
    inset: 0;
    background:
      radial-gradient(ellipse at 70% 65%, var(--blush) 0%, rgba(243,228,234,0) 45%),
      linear-gradient(160deg, var(--paper) 0%, var(--mist) 55%, #dcdde0 100%);
  }
  .contact {
    position: absolute;
    left: 250px;
    top: 150px;
    color: var(--ink);
  }
  .contact__name {
    margin: 0 0 16px;
    font-size: 29px;
    font-weight: 400;
  }
  .contact__line {
    margin: 0 0 6px;
    font-size: 17px;
  }
</style>
</head>
<body>
<main class="canvas">
  <section class="card card--front">
    <div class="front-texture" role="img" aria-label="Fond bleu nuit avec rayons lumineux rayonnant depuis le centre"></div>
    <div class="front-lockup">
      <h1 class="brand">Lumenweave</h1>
      <p class="tagline">Cabinet de conseil en aménagement intérieur</p>
    </div>
  </section>

  <section class="card card--back">
    <div class="back-photo" role="img" aria-label="Photographie pâle de verres en cristal et de roses roses sur une table blanche"></div>
    <div class="contact">
      <h2 class="contact__name">Claire-Anne Vobrel</h2>
      <p class="contact__line">P: + 33 6 91 35 20 86</p>
      <p class="contact__line">E: cavobrel@postvane.fr</p>
    </div>
  </section>
</main>
</body>
</html>
```